Nordic Forgecraft Guild Wordpress Theme and newsletter template

We at the NFG are looking to start a Wordpress website and also send out a newsletter (web). We have just completed a Logo design project with ArtMarketo and we were so pleased with the results that we would like to see what the designers can come up with for a Wordpress theme and a template for an online newsletter. The theme has to support Icelandic letters. It also has to have a subscription option by email. We would need to have the option to add advertisement banners. The theme has to be easy to work with.
Below we have added a two websites for a example of what we are looking for: .
http://www.brazecouncil.example/
http://www.lodning.example/
The newsletter has to have a similar theme as the website and will be used with MS Publisher.

Target Market(s)

Welding association members, welding and metalworking industry, suppliers in welding industry, International welding community, other national welding associations, welding education community

Industry/Entity Type

Welding

Number of Pages Required

3 page

Requirements
Must have
• The RÞKL logo
• Icelandic letters
• email formpage
• Advertisement space/banners/buttons
• Easy to manage
• Compatible with Wordpress
Nice to have
• Welding pictures
• Nice graphics
Should not have
• Should not be dark and heavy set.

```html
<!DOCTYPE html>
<html lang="is">
<head>
<meta charset="utf-8">
<title>Nordic Forgecraft Guild — Theme</title>
<link href="https://fonts.googleapis.com/css2?family=Open+Sans:ital,wght@0,400;0,600;0,700;1,400&display=swap" rel="stylesheet">
<style>
  :root {
    --blue: #1a9ad9;
    --blue-button: #2593d6;
    --grey-text: #5a5a5a;
    --nav-text: #4a4a4a;
    --banner-grey: #e6e6e6;
    --panel-tint: #faf6f7;
    --footer-bg: #a6dbee;
    --white: #ffffff;
    --hero-dark: #0b0e18;
    --hero-mid: #1d2434;
  }
  * { box-sizing: border-box; margin: 0; padding: 0; }
  html, body { width: 1200px; height: 2394px; overflow: hidden; }
  body {
    position: relative;
    background: var(--white);
    font-family: "Open Sans", Arial, sans-serif;
    color: var(--grey-text);
  }
  .abs { position: absolute; }

  /* Header */
  .site-header { position: absolute; left: 0; top: 0; width: 1200px; height: 131px; background: var(--white); border-left: 2px solid #222; }
  .brand { position: absolute; left: 214px; top: 38px; display: flex; flex-direction: column; }
  .brand-name { font-size: 40px; font-weight: 700; color: var(--blue); line-height: 1; letter-spacing: 1px; }
  .brand-sub { font-size: 8.5px; font-weight: 700; color: var(--blue); letter-spacing: .3px; margin-top: 3px; }
  .main-nav a { position: absolute; top: 59px; font-size: 13px; color: var(--nav-text); text-decoration: none; letter-spacing: .4px; }
  .search-icon { position: absolute; left: 990px; top: 57px; }

  /* Hero */
  .hero-bg { position: absolute; left: 0; top: 131px; }
  .hero-title { position: absolute; left: 0; width: 1200px; top: 265px; text-align: center; color: var(--white); font-size: 25px; font-weight: 600; letter-spacing: .3px; }
  .subscribe-input { position: absolute; left: 337px; top: 360px; width: 335px; height: 38px; background: var(--white); border: none; border-radius: 2px; padding-left: 12px; font-family: inherit; font-size: 12px; font-style: italic; color: #aaa; display: flex; align-items: center; }
  .subscribe-button { position: absolute; left: 677px; top: 360px; width: 135px; height: 38px; background: var(--blue-button); color: var(--white); font-size: 12.5px; display: flex; align-items: center; justify-content: center; border-radius: 2px; }

  /* Ad banners */
  .ad-banner { position: absolute; background: var(--banner-grey); color: var(--white); display: flex; flex-direction: column; align-items: center; justify-content: center; font-size: 25px; line-height: 1.55; }

  /* Intro section */
  .section-heading { position: absolute; color: var(--blue); font-weight: 600; text-align: center; }
  .body-copy { position: absolute; font-size: 12.6px; font-weight: 600; line-height: 16px; text-align: justify; color: var(--grey-text); }
  .body-copy p + p { margin-top: 14px; }
  .indent { text-indent: 26px; }

  /* News preview */
  .news-shapes { position: absolute; left: 0; top: 1000px; }
  .news-copy { line-height: 21px; text-align: left; }
  .read-more { position: absolute; left: 910px; top: 1460px; font-size: 12.5px; font-weight: 700; color: var(--blue); }

  /* Footer */
  .site-footer { position: absolute; left: 0; top: 2190px; width: 1200px; height: 204px; background: var(--footer-bg); }
  .footer-brand { position: absolute; left: 212px; top: 44px; }
  .footer-brand .brand-name { font-size: 64px; }
  .footer-brand .brand-sub { font-size: 10px; margin-top: 6px; }
  .footer-col { position: absolute; top: 54px; display: flex; flex-direction: column; gap: 11px; }
  .footer-col a { color: var(--white); font-size: 12.5px; font-weight: 600; text-decoration: none; line-height: 17px; }
</style>
</head>
<body>

<header class="site-header">
  <div class="brand">
    <span class="brand-name">RÞKL</span>
    <span class="brand-sub">SMIÐJUFÉLAG NORÐURLANDA</span>
  </div>
  <nav class="main-nav">
    <a style="left:413px">HOME</a>
    <a style="left:522px">ABOUT</a>
    <a style="left:624px">SERVICES</a>
    <a style="left:752px">CONTACT</a>
  </nav>
  <svg class="search-icon" width="16" height="16" viewBox="0 0 16 16" aria-label="Search">
    <circle cx="6.5" cy="6.5" r="4.8" fill="none" stroke="#444" stroke-width="2"/>
    <line x1="10" y1="10" x2="14.5" y2="14.5" stroke="#444" stroke-width="2.2" stroke-linecap="round"/>
  </svg>
</header>

<svg class="hero-bg" width="1200" height="474" viewBox="0 0 1200 474" role="img" aria-label="Photo of a welder at work with sparks and smoke">
  <defs>
    <linearGradient id="heroGrad" x1="0" y1="0" x2="1" y2="1">
      <stop offset="0" stop-color="#2a2f3c"/>
      <stop offset=".45" stop-color="var(--hero-dark)"/>
      <stop offset=".75" stop-color="#1f2a4a"/>
      <stop offset="1" stop-color="#3a3430"/>
    </linearGradient>
  </defs>
  <polygon points="0,0 1200,0 1200,472 0,356" fill="url(#heroGrad)"/>
</svg>
<h1 class="hero-title">ENTER YOUR EMAIL TO GET LATEST COMMUNITY NEWS!</h1>
<div class="subscribe-input">Your e-mail</div>
<div class="subscribe-button">Get Latest News</div>

<div class="ad-banner" style="left:187px; top:589px; width:212px; height:424px;">
  <span>300x600</span><span>ad banner</span>
</div>
<h2 class="section-heading" style="left:452px; width:525px; top:630px; font-size:28px;">HEADING</h2>
<div class="body-copy" style="left:452px; top:765px; width:560px;">
  <p>Lorem ipsum dolor sit amet, consectetur adipisicing elit, sed do eiusmod tempor incididunt ut labore et dolore magna aliqua. Ut enim ad minim veniam, quis nostrud exercitation ullamco laboris nisi ut aliquip ex ea commodo consequat. Duis aute irure dolor in reprehenderit in voluptate velit esse cillum dolore eu fugiat nulla pariatur. Excepteur sint occaecat cupidatat non proident, sunt in culpa qui officia deserunt mollit anim id est laborum</p>
  <p class="indent">Lorem ipsum dolor sit amet, consectetur adipisicing elit, sed do eiusmod tempor incididunt ut labore et dolore magna aliqua. Ut enim ad minim veniam, quis nostrud exercitation ullamco laboris nisi ut aliquip ex ea commodo consequat. Duis aute irure dolor in reprehenderit in voluptate velit esse cillum dolore eu fugiat nulla pariatur. Excepteur sint occaecat cupidatat non proident, sunt in culpa qui officia deserunt mollit anim id est laborum..</p>
</div>

<svg class="news-shapes" width="1200" height="630" viewBox="0 0 1200 630">
  <defs>
    <linearGradient id="photoGrad" x1="0" y1="0" x2="1" y2="1">
      <stop offset="0" stop-color="#d9dbdd"/>
      <stop offset=".5" stop-color="#eeeeef"/>
      <stop offset="1" stop-color="#c9cbcd"/>
    </linearGradient>
  </defs>
  <polygon points="590,70 1200,12 1200,618 590,548" fill="var(--panel-tint)"/>
  <polygon points="0,122 590,98 590,548 0,484" fill="url(#photoGrad)" role="img" aria-label="Photo of a welder in a helmet working in a workshop"/>
</svg>
<h2 class="section-heading" style="left:610px; width:370px; top:1158px; font-size:23.5px;">Latest News Post Preview</h2>
<div class="body-copy news-copy" style="left:611px; top:1248px; width:385px;">
  <p>Lorem ipsum dolor sit amet, consectetur adipisicing elit, sed do eiusmod tempor incididunt ut labore et dolore magna aliqua. Ut enim ad minim veniam, quis nostrud exercitation ullamco laboris nisi ut aliquip ex ea commodo consequat. Duis aute irure dolor in reprehenderit in voluptate velit esse cillum dolore eu fugiat nulla pariatur. Excepteur sint occaecat cupidatat non proident, sunt in culpa qui officia deserunt mollit anim id est laborum.</p>
</div>
<span class="read-more">Read more...</span>

<h2 class="section-heading" style="left:0; width:1214px; top:1677px; font-size:28px;">ABOUT COMMUNITY</h2>
<div class="body-copy" style="left:216px; top:1815px; width:750px; line-height:21px;">
  <p class="indent">Lorem ipsum dolor sit amet, consectetur adipisicing elit, sed do eiusmod tempor incididunt ut labore et dolore magna aliqua. Ut enim ad minim veniam, quis nostrud exercitation ullamco laboris nisi ut aliquip ex ea commodo consequat. Duis aute irure dolor in reprehenderit in voluptate velit esse cillum dolore eu fugiat nulla pariatur. Excepteur sint occaecat cupidatat non proident, sunt in culpa qui officia deserunt mollit anim id est laborum.</p>
  <p class="indent" style="margin-top:22px;">Lorem ipsum dolor sit amet, consectetur adipisicing elit, sed do eiusmod tempor incididunt ut labore et dolore magna aliqua. Ut enim ad minim veniam, quis nostrud exercitation ullamco laboris nisi ut aliquip ex ea commodo consequat. Duis aute irure dolor in reprehenderit in voluptate velit esse cillum dolore eu fugiat nulla pariatur. Excepteur sint occaecat cupidatat non proident, sunt in culpa qui officia deserunt mollit anim id est laborum</p>
</div>

<div class="ad-banner" style="left:260px; top:2067px; width:686px; height:86px; line-height:1.45;">
  <span>970x120</span><span>ad banner</span>
</div>

<footer class="site-footer">
  <div class="brand footer-brand">
    <span class="brand-name">RÞKL</span>
    <span class="brand-sub">SMIÐJUFÉLAG NORÐURLANDA</span>
  </div>
  <nav class="footer-col" style="left:476px;"><a>Home</a><a>About</a><a>Services</a><a>Contact</a></nav>
  <nav class="footer-col" style="left:609px;"><a>Home</a><a>About</a><a>Services</a><a>Contact</a></nav>
  <nav class="footer-col" style="left:742px;"><a>Home</a><a>About</a><a>Services</a><a>Contact</a></nav>
</footer>

</body>
</html>
```